Business Card For Kelmora Financial Consulting

Hi, I would like a business card designed. Bold, modern.
Please use the same design as the logo. I have also attached the website design to see the overall theme.
Wordmark Font
Color: Hex: #01AEF7

```html
<!DOCTYPE html>
<html lang="en">
<head>
<meta charset="utf-8">
<title>Kelmora Financial Consulting — Business Card</title>
<link rel="stylesheet" href="https://fonts.googleapis.com/css2?family=Montserrat:wght@400;500;700;800&display=swap">
<style>
  :root {
    --backdrop: #8c8c8c;
    --card: #16222c;
    --accent: #01aef7;
    --accent-soft: #3aa9e0;
    --ink: #ffffff;
  }
  * { margin: 0; padding: 0; box-sizing: border-box; }
  html, body { width: 1160px; height: 1200px; overflow: hidden; }
  body {
    background: var(--backdrop);
    font-family: "Montserrat", Arial, sans-serif;
    color: var(--ink);
    position: relative;
  }
  .card {
    position: absolute;
    left: 199px;
    width: 777px;
    height: 442px;
    background: var(--card);
    border-radius: 28px;
  }
  .card--front { top: 105px; }
  .card--back { top: 634px; }

  /* brand wordmark (text only, one colour, one weight) */
  .brand {
    position: absolute;
    text-align: center;
    font-weight: 700;
    color: var(--ink);
    line-height: 1;
    white-space: nowrap;
  }
  .brand span { display: block; }
  .card--front .brand { left: 40px; top: 206px; width: 320px; }
  .card--front .brand__main { font-size: 37px; letter-spacing: 6px; text-indent: 6px; }
  .card--front .brand__sub { font-size: 10px; letter-spacing: 15px; text-indent: 15px; margin-top: 9px; }

  .card--back .brand { left: 0; top: 176px; width: 777px; }
  .card--back .brand__main { font-size: 60px; letter-spacing: 8px; text-indent: 8px; }
  .card--back .brand__sub { font-size: 18px; letter-spacing: 23px; text-indent: 23px; margin-top: 16px; }

  /* divider */
  .divider {
    position: absolute;
    width: 1.5px;
    background: var(--accent-soft);
  }
  .divider--short-left { left: 378px; top: 137px; height: 163px; }
  .divider--tall { left: 392px; top: 98px; height: 247px; }
  .divider--short-right { left: 404px; top: 137px; height: 163px; }

  /* contact block */
  .person {
    position: absolute;
    left: 441px;
    top: 96px;
  }
  .person__name {
    font-size: 31px;
    font-weight: 800;
    color: var(--accent-soft);
    line-height: 1;
    letter-spacing: 0.2px;
  }
  .person__role {
    font-size: 19px;
    font-weight: 400;
    margin-top: 7px;
  }
  .person__address {
    font-size: 19px;
    font-weight: 500;
    line-height: 28px;
    margin-top: 16px;
    font-style: normal;
  }
  .contacts {
    position: absolute;
    left: 441px;
    top: 247px;
    list-style: none;
  }
  .contacts__item {
    display: flex;
    align-items: center;
    gap: 8px;
    height: 24px;
    margin-bottom: 13.5px;
    font-size: 19px;
    font-weight: 500;
  }
  .contacts__icon { width: 24px; height: 24px; flex: none; }
</style>
</head>
<body>

  <section class="card card--front" aria-label="Business card front">
    <div class="brand">
      <span class="brand__main">KELMORA</span>
      <span class="brand__sub">CONSULTING</span>
    </div>

    <div class="divider divider--short-left"></div>
    <div class="divider divider--tall"></div>
    <div class="divider divider--short-right"></div>

    <div class="person">
      <h1 class="person__name">TOVIN HARWELL</h1>
      <p class="person__role">Senior Consultant</p>
      <address class="person__address">42-07 Larkspur Ave 14<br>Ridgefield, NY 11470</address>
    </div>

    <ul class="contacts">
      <li class="contacts__item">
        <svg class="contacts__icon" viewBox="0 0 24 24" aria-hidden="true">
          <circle cx="12" cy="12" r="12" fill="var(--accent-soft)"/>
          <path d="M6 10c0-2 3-3 6-3s6 1 6 3l-2 1-1-2h-6l-1 2z" fill="#fff"/>
          <rect x="8" y="11" width="8" height="6" rx="1" fill="#fff"/>
        </svg>
        <span>+1 555 214 7730</span>
      </li>
      <li class="contacts__item">
        <svg class="contacts__icon" viewBox="0 0 24 24" aria-hidden="true">
          <circle cx="12" cy="12" r="12" fill="var(--accent-soft)"/>
          <rect x="6" y="8" width="12" height="8" fill="#fff"/>
          <path d="M6 8l6 5 6-5" fill="none" stroke="var(--accent-soft)" stroke-width="1.2"/>
        </svg>
        <span>hello@kelmoraconsult.com</span>
      </li>
      <li class="contacts__item">
        <svg class="contacts__icon" viewBox="0 0 24 24" aria-hidden="true">
          <circle cx="12" cy="12" r="12" fill="var(--accent-soft)"/>
          <circle cx="12" cy="12" r="6.5" fill="none" stroke="#fff" stroke-width="1.4"/>
          <ellipse cx="12" cy="12" rx="2.8" ry="6.5" fill="none" stroke="#fff" stroke-width="1.2"/>
          <path d="M5.5 12h13" stroke="#fff" stroke-width="1.2"/>
        </svg>
        <span>www.kelmoraconsult.com</span>
      </li>
    </ul>
  </section>

  <section class="card card--back" aria-label="Business card back">
    <div class="brand">
      <span class="brand__main">KELMORA</span>
      <span class="brand__sub">CONSULTING</span>
    </div>
  </section>

</body>
</html>
```